HVAC company business card design

We need a business card design for a HVAC company. The design must look professional. Both sides will be used. The total data to be on the business card is
Name
Position
Email
Direct Phone/Moile Phone
Company Contacts /Address, Phone, Fax, web)
All data will be submit once the design is confirmed. For generic purposes use;
Emre Toksoy
Managing Director
+902324815263 (Mobile)
4712 Sokak No: 9 KBSE Yenikent IZMIR TURKEY
Tel: +902324815263 Fax : +902324815269
www.luvon.com.tr

Target Market(s)

HVAC

Industry/Entity Type

Business

Contact Information for Business Card

The total data to be on the business card is
Name
Position
Email
Direct Phone/Moile Phone
Emre Toksoy
Managing Director
+902324815263 (Mobile)
www.luvon.com.tr
The BC will use both sides of the card. The front will include the full logo and the details for the business card holder. The business card can be divided into vertical/horizontal or to a special shape. The common data like the company address/phone/fax should be indicated elsewehere. The back can contain some part or the whole logo and must contain the web address.

Font styles to use
Serif
Sans Serif

Colors
0355a3
cfdfed

Requirements
Should not have
• Please be careful with the fonts, it shouldnt be too small or too big and must not interfere with the logo fonts. If you need to use a curvy shape please do not use as the logo is already curvy or use the curves from the logo (if it looks good, otherwise forget it)
• We are not in favor of pictograms, only if they are perfect use them.

```html
<!DOCTYPE html>
<html lang="en">
<head>
<meta charset="utf-8">
<title>LUVON Business Card</title>
<link rel="stylesheet" href="https://fonts.googleapis.com/css2?family=Open+Sans:wght@400;600;700&display=swap">
<style>
  :root {
    --brand-blue: #0355a3;
    --brand-blue-deep: #02447f;
    --brand-blue-soft: #cfdfed;
    --brand-blue-mid: #4f86c6;
    --ink-slate: #44536a;
    --ink-dark: #2b2f36;
    --mark-light: #d3dbe4;
    --paper: #ffffff;
    --stage: #e8ecf0;
  }
  * { box-sizing: border-box; margin: 0; padding: 0; }
  html, body {
    width: 1200px;
    height: 900px;
    overflow: hidden;
    background: var(--stage);
    font-family: "Open Sans", Arial, sans-serif;
  }
  .canvas {
    position: relative;
    width: 1200px;
    height: 900px;
  }
  .card {
    position: absolute;
    left: 250px;
    width: 700px;
    height: 400px;
    overflow: hidden;
    box-shadow: 0 10px 28px rgba(20, 40, 70, 0.18);
  }

  /* Back side */
  .card-back {
    top: 30px;
    background: linear-gradient(160deg, var(--brand-blue) 0%, var(--brand-blue-deep) 100%);
  }
  .card-back .back-disc {
    position: absolute;
    left: 40px;
    top: 60px;
    width: 290px;
    height: 290px;
    border-radius: 50%;
    background: radial-gradient(circle at 40% 35%, #5f95d2 0%, var(--brand-blue-mid) 55%, #2f6db3 100%);
  }
  .card-back .back-name {
    position: absolute;
    right: 48px;
    top: 120px;
    font-size: 70px;
    font-weight: 600;
    letter-spacing: 4px;
    color: var(--mark-light);
  }
  .card-back .back-web {
    position: absolute;
    right: 52px;
    top: 212px;
    font-size: 20px;
    font-weight: 400;
    color: var(--brand-blue-soft);
    letter-spacing: 0.5px;
  }

  /* Front side */
  .card-front {
    top: 470px;
    background: var(--paper);
  }
  .card-front .front-wave {
    position: absolute;
    left: 0;
    top: 0;
    width: 700px;
    height: 400px;
  }
  .brand {
    position: absolute;
    left: 48px;
    top: 128px;
    display: flex;
    align-items: center;
    gap: 16px;
  }
  .brand-dot {
    width: 62px;
    height: 62px;
    border-radius: 50%;
    background: var(--brand-blue-mid);
  }
  .brand-name {
    font-size: 58px;
    font-weight: 600;
    letter-spacing: 3px;
    color: var(--ink-slate);
    line-height: 1;
  }
  .divider {
    position: absolute;
    left: 418px;
    top: 56px;
    width: 1px;
    height: 160px;
    background: linear-gradient(var(--brand-blue-soft), var(--brand-blue-mid), var(--brand-blue-soft));
  }
  .holder {
    position: absolute;
    left: 440px;
    top: 40px;
    color: var(--ink-dark);
  }
  .holder-name {
    font-size: 19px;
    font-weight: 700;
    color: var(--brand-blue);
    line-height: 1.2;
  }
  .holder-role {
    font-size: 14px;
    font-weight: 400;
    margin-bottom: 14px;
  }
  .holder-address {
    font-size: 14px;
    line-height: 1.3;
    margin-bottom: 10px;
  }
  .contact-list {
    list-style: none;
  }
  .contact-list li {
    display: flex;
    align-items: center;
    gap: 12px;
    font-size: 15px;
    line-height: 1.55;
  }
  .contact-list .web {
    font-weight: 600;
  }
  .contact-icon {
    width: 14px;
    height: 14px;
    flex: none;
    fill: var(--brand-blue);
  }
</style>
</head>
<body>
<main class="canvas">

  <section class="card card-back" aria-label="Card back">
    <div class="back-disc"></div>
    <div class="back-name">LUVON</div>
    <div class="back-web">www.luvon.com.tr</div>
  </section>

  <section class="card card-front" aria-label="Card front">
    <svg class="front-wave" viewBox="0 0 700 400" aria-hidden="true">
      <defs>
        <linearGradient id="band-fill" x1="0" y1="0" x2="1" y2="0">
          <stop offset="0" stop-color="#0a5fb0"/>
          <stop offset="1" stop-color="#0355a3"/>
        </linearGradient>
      </defs>
      <path d="M0,222 C140,300 400,352 700,340 L700,400 L0,400 Z" fill="#cfdfed"/>
      <path d="M0,248 C150,322 410,372 700,360 L700,400 L0,400 Z" fill="url(#band-fill)"/>
    </svg>

    <div class="brand">
      <span class="brand-dot"></span>
      <span class="brand-name">LUVON</span>
    </div>

    <div class="divider"></div>

    <div class="holder">
      <p class="holder-name">Emre Toksoy</p>
      <p class="holder-role">Managing Director</p>
      <p class="holder-address">4712 Sokak No: 9 KBSE<br>Yenikent IZMIR TURKEY</p>
      <ul class="contact-list">
        <li>
          <svg class="contact-icon" viewBox="0 0 14 14" aria-label="Mobile"><rect x="3.5" y="0.5" width="7" height="13" rx="1.5"/><rect x="4.8" y="2" width="4.4" height="8" fill="#fff"/></svg>
          +902324815263
        </li>
        <li>
          <svg class="contact-icon" viewBox="0 0 14 14" aria-label="Phone"><path d="M3 1 L5.5 1 L6.5 4 L5 5.2 C5.8 7 7 8.2 8.8 9 L10 7.5 L13 8.5 L13 11 C13 12.2 12 13 10.8 13 C5.6 12.6 1.4 8.4 1 3.2 C1 2 1.8 1 3 1 Z"/></svg>
          +902324815263
        </li>
        <li>
          <svg class="contact-icon" viewBox="0 0 14 14" aria-label="Fax"><rect x="3.5" y="1" width="7" height="4"/><rect x="1" y="5" width="12" height="6" rx="1"/><rect x="3.5" y="9" width="7" height="4" fill="#fff" stroke="#0355a3" stroke-width="1"/></svg>
          +902324815269
        </li>
        <li class="web">
          <svg class="contact-icon" viewBox="0 0 14 14" aria-label="Website"><circle cx="7" cy="7" r="6" fill="none" stroke="#0355a3" stroke-width="1.4"/><ellipse cx="7" cy="7" rx="2.6" ry="6" fill="none" stroke="#0355a3" stroke-width="1.1"/><line x1="1" y1="7" x2="13" y2="7" stroke="#0355a3" stroke-width="1.1"/></svg>
          www.luvon.com.tr
        </li>
      </ul>
    </div>
  </section>

</main>
</body>
</html>
```